High profile consulting company needs a Business Card Design

I need a business card design for a coaching /consulting company. We specialize in changing behaviors. Our services include therapy, workshops, life coaching, etc.

Check out our website to get a feel for our personality. www.tidewellpartners.com

The new logo will be attached to the website soon, I have attached the new logo for your use on the business card.
Updates

I forgot to provide you with the company email under the "must have" section for the business card.  The website is:

 www.tidewellpartners.com

I understand there's some trouble with the logo I uploaded.  I will try that again.  Thank you for your efforts.

Dalia

Thank you for some of your questions.  I prefer a one sided business card, and tend to like the white backgrounds.

I also made 2 small changes to the content.  

add MFT after the name:  Dalia Forsythe, MFT

and the tag line needed more clarity once I saw it.  Please change it to:  Improving performance by strengthening relationships and changing behaviors.

Thank you,
Dalia

Industry/Entity Type

Business

Requirements
Must have
• logo
Phone number: 321-555-0148
email: Dalia@tidewellpartners.com
Dalia Forsythe, MFT
President
Nice to have
• Improving performance by strengthening relationships and changing behaviors.

```html
<!DOCTYPE html>
<html lang="en">
<head>
<meta charset="utf-8">
<title>Tidewell Partners – Business Card</title>
<link rel="stylesheet" href="https://fonts.googleapis.com/css2?family=Montserrat:wght@400;700&display=swap">
<style>
  :root {
    --page-bg: #ffffff;
    --card-bg: #ffffff;
    --card-edge: #cfd0d2;
    --brand-green: #14784f;
    --steel-grey: #7c7e81;
    --mist-grey: #d2d3d5;
    --ink-light: #ffffff;
  }
  * { margin: 0; padding: 0; box-sizing: border-box; }
  html, body {
    width: 900px;
    height: 1200px;
    overflow: hidden;
    background: var(--page-bg);
  }
  .canvas {
    position: relative;
    width: 900px;
    height: 1200px;
  }
  .business-card {
    position: absolute;
    left: 26px;
    top: 300px;
    width: 844px;
    height: 510px;
    background: var(--card-bg);
    border: 1px solid var(--card-edge);
    overflow: hidden;
    font-family: "Montserrat", sans-serif;
  }
  .brand {
    position: absolute;
    left: 122px;
    top: 84px;
    display: flex;
    align-items: center;
    gap: 30px;
  }
  .brand-dot {
    width: 150px;
    height: 150px;
    border-radius: 50%;
    background: var(--brand-green);
    flex: none;
  }
  .brand-name {
    color: var(--brand-green);
    font-weight: 700;
    font-size: 50px;
    line-height: 1.05;
    letter-spacing: 1px;
    text-transform: uppercase;
  }
  .title-band {
    position: absolute;
    left: 0;
    top: 314px;
    width: 100%;
    height: 62px;
  }
  .title-band svg {
    position: absolute;
    inset: 0;
  }
  .person-title {
    position: absolute;
    right: 26px;
    top: 0;
    height: 62px;
    display: flex;
    align-items: center;
    color: var(--ink-light);
    font-size: 38px;
    font-weight: 400;
  }
  .contact-band {
    position: absolute;
    left: 0;
    top: 376px;
    width: 100%;
    height: 134px;
    background: var(--brand-green);
    padding: 14px 26px 0 0;
    text-align: right;
    color: var(--ink-light);
  }
  .contact-line {
    font-size: 27px;
    line-height: 34px;
    font-weight: 400;
  }
</style>
</head>
<body>
<main class="canvas">
  <section class="business-card">
    <div class="brand">
      <div class="brand-dot"></div>
      <div class="brand-name">Tidewell<br>Partners</div>
    </div>

    <div class="title-band">
      <svg width="844" height="62" viewBox="0 0 844 62" aria-hidden="true">
        <polygon points="0,0 186,0 146,62 0,62" fill="var(--mist-grey)"/>
        <polygon points="196,0 844,0 844,62 156,62" fill="var(--steel-grey)"/>
      </svg>
      <p class="person-title">Dalia Forsythe, President</p>
    </div>

    <div class="contact-band">
      <p class="contact-line">Email: Dalia@tidewellpartners.com</p>
      <p class="contact-line">Phone: 321-555-0148</p>
      <p class="contact-line">www.tidewellpartners.com</p>
    </div>
  </section>
</main>
</body>
</html>
```